Ember Relaywork - Field Service Brochure

We are looking for a one page marketing brochure that includes our rate sheet. I've attached the working we on on the rate page, several photos and several versions of our logo.

```html
<!DOCTYPE html>
<html lang="en">
<head>
<meta charset="utf-8">
<title>Ember Relaywork – Field Service Brochure</title>
<link rel="stylesheet" href="https://fonts.googleapis.com/css2?family=Montserrat:wght@400;500;700&family=Tinos&display=swap">
<style>
  :root {
    --bg: #c9c5c6;
    --paper: #f6f7f9;
    --ink: #1e2a36;
    --steel: #466d8a;
    --steel-light: #5f8aa6;
    --steel-dark: #34566f;
    --sky-top: #0f2250;
    --sky-bottom: #425067;
    --white: #ffffff;
  }
  * { margin: 0; padding: 0; box-sizing: border-box; }
  html, body { width: 1200px; height: 948px; overflow: hidden; background: var(--bg); }
  body { font-family: "Montserrat", sans-serif; color: var(--ink); }

  .brochure {
    position: absolute; left: 252px; top: 24px;
    width: 696px; height: 900px;
    background: linear-gradient(160deg, var(--white) 0%, var(--paper) 60%, #e9edf1 100%);
    box-shadow: 0 8px 28px rgba(0,0,0,.25);
    overflow: hidden;
  }
  .art { position: absolute; inset: 0; width: 696px; height: 900px; }

  .masthead { position: absolute; left: 52px; top: 44px; display: flex; align-items: center; gap: 14px; }
  .masthead-mark { width: 26px; height: 26px; background: var(--ink); }
  .masthead-name { font-family: "Tinos", serif; font-size: 27px; color: var(--ink); white-space: nowrap; }

  .rates {
    position: absolute; left: 446px; top: 350px; width: 236px;
    color: var(--white); font-size: 11px; line-height: 1.35;
  }
  .rates h3 { font-size: 12.5px; font-weight: 700; text-decoration: underline; display: inline; }
  .rates p { margin-bottom: 6px; }
  .rates ul { list-style: none; margin-bottom: 10px; }
  .rates li { position: relative; padding-left: 12px; margin-bottom: 5px; }
  .rates li::before { content: "•"; position: absolute; left: 0; }
  .rates b { font-weight: 700; font-size: 12px; }

  .intro { position: absolute; left: 40px; top: 518px; width: 370px; font-size: 10.5px; line-height: 1.4; }
  .intro p { margin-bottom: 12px; }

  .section-title {
    color: var(--steel); font-weight: 700; font-size: 14px;
    text-decoration: underline; margin-bottom: 3px;
  }
  .list { list-style: none; font-size: 10.5px; line-height: 1.4; }
  .list li { position: relative; padding-left: 12px; }
  .list li::before { content: "•"; position: absolute; left: 0; }

  .expenses { position: absolute; left: 40px; top: 650px; width: 390px; }
  .minimum { position: absolute; left: 40px; top: 754px; width: 620px; }

  .footer {
    position: absolute; left: 0; right: 0; bottom: 0; height: 36px;
    background: var(--steel); color: var(--white);
    font-size: 11px; font-weight: 500;
    display: flex; align-items: center; justify-content: center; letter-spacing: .2px;
  }
  .footer-rule { position: absolute; left: 0; right: 0; bottom: 42px; height: 3px; background: var(--steel); }
</style>
</head>
<body>
  <main class="brochure">
    <svg class="art" viewBox="0 0 696 900" xmlns="http://www.w3.org/2000/svg">
      <defs>
        <linearGradient id="sky" x1="0" y1="0" x2="0" y2="1">
          <stop offset="0" stop-color="#0f2250"/>
          <stop offset="1" stop-color="#46505f"/>
        </linearGradient>
        <linearGradient id="crew" x1="0" y1="0" x2="1" y2="1">
          <stop offset="0" stop-color="#5e8ec6"/>
          <stop offset=".6" stop-color="#9aa6ad"/>
          <stop offset="1" stop-color="#c06a3a"/>
        </linearGradient>
        <linearGradient id="field" x1="0" y1="0" x2="1" y2="1">
          <stop offset="0" stop-color="#cdbb95"/>
          <stop offset=".5" stop-color="#6f8a4a"/>
          <stop offset="1" stop-color="#8f9aa3"/>
        </linearGradient>
      </defs>

      <!-- masthead rules -->
      <line class="rule" x1="250" y1="34" x2="650" y2="34" stroke="#1e2a36" stroke-width="1.5"/>
      <line class="rule" x1="40" y1="88" x2="650" y2="88" stroke="#1e2a36" stroke-width="1.5"/>

      <!-- main photo -->
      <polygon role="img" aria-label="Photo of field technicians on an orange lift working on substation switchgear against a dark blue sky"
               points="0,112 540,112 330,452 0,452" fill="url(#sky)"/>
      <!-- accent strip -->
      <polygon points="548,112 566,112 432,330 432,360" fill="var(--steel-light)"/>
      <!-- rate panel -->
      <polygon points="572,112 696,112 696,652 432,652 432,340" fill="var(--steel)"/>

      <!-- hexagon photos -->
      <polygon role="img" aria-label="Photo of technician in safety vest servicing equipment outdoors"
               points="592,124 666,124 696,186 666,248 592,248 562,186"
               fill="url(#field)" stroke="#fff" stroke-width="4"/>
      <polygon role="img" aria-label="Photo of technician on a lift beside substation frame"
               points="60,392 140,392 178,452 140,512 60,512 22,452"
               fill="url(#crew)" stroke="#fff" stroke-width="4"/>
      <polygon role="img" aria-label="Photo of crew working on switchgear with orange lift"
               points="210,392 290,392 328,452 290,512 210,512 172,452"
               fill="url(#crew)" stroke="#fff" stroke-width="4"/>
    </svg>

    <header class="masthead">
      <span class="masthead-mark"></span>
      <span class="masthead-name">Ember Relaywork Manufacturing Co.</span>
    </header>

    <section class="rates">
      <p><h3>Standard Rates</h3> (on-site) up to 10 hours + travel and per diem expenses</p>
      <ul>
        <li><b>$250 x 1.00</b> = Monday through Friday rate per hour ($2500 minimum)</li>
        <li><b>$250 x 1.50</b> = Saturday rate per hour</li>
        <li><b>$250 X 2.00</b> = Sunday rate per hour</li>
      </ul>
      <p><h3>Premium Rates</h3> (on-site) over 8 hours +travel and per diem expenses</p>
      <ul>
        <li><b>$250 X 1.50</b> = Over Time (9-12 hours) rate per hour</li>
        <li><b>$250 x 2.00</b> = Double Time (Over 12 hours) rate per hour</li>
        <li><b>$250 X 2.50</b> = Non-standard overnight hours</li>
      </ul>
    </section>

    <section class="intro">
      <p>Ember Relaywork Company offers an expertly trained Field Service program that can provide technical guidance and assistance for your initial installation, sustaining maintenance, and repair of equipment manufactured by Ember Relaywork.</p>
      <p>A 4-6 week reservation for assistance is recommended to ensure that we can fully accommodate your desired schedule. Expedited service may be available upon request.</p>
    </section>

    <section class="expenses">
      <h2 class="section-title">EXPENSES</h2>
      <ul class="list">
        <li>Airfare - invoiced at actual cost + 25%</li>
        <li>Lodging - invoiced at actual cost + 25%</li>
        <li>Meals and Incidentals - invoiced at cost (not to exceed $100/day)</li>
        <li>Rental Vehicle and related costs - Invoiced at cost +25%</li>
      </ul>
    </section>

    <section class="minimum">
      <h2 class="section-title">MINIMUM CHARGE</h2>
      <ul class="list">
        <li>The minimum charge, excluding travel time and expenses shall be the equivalent of one 10 hour day</li>
        <li>Cancellation charge of 4 standard hours plus any non-cancellable airfare or lodging charges shall apply</li>
        <li>Employee Drug Screening</li>
        <li>Drug screening and/or background check costs (if required by customer) shall be invoiced at actual cost plus 30%.</li>
      </ul>
    </section>

    <div class="footer-rule"></div>
    <footer class="footer">1480 Alder Court N.W. • Fairvale, AL 35900 • 205-555-0142 • 800-555-0177 • Fax: 205-555-0196</footer>
  </main>
</body>
</html>
```